Business Card Design Project

We recently redesigned our corporate logo and are looking for a business card refreshment.

The business card template should have a place for the following:
Name, Title, email, phone number, instant messenger handle, and the vitals of the company such as the address, main line, web site etc.

PLEASE DO NOT USE OUR EXISTING WEB SITE FOR INSPIRATION as we are redesigning it.

We've attached a picture of our existing business card as an example, although please keep in mind that we have changed the logo (also attached) and encourage your creativity.

Target Market(s)

Information scientists, search professionals, technical people, Ph.Ds, and executives

Industry/Entity Type

Business

Requirements
Must have
• We'll need the template in a format like Illustrator.

```html
<!DOCTYPE html>
<html lang="en">
<head>
<meta charset="utf-8">
<title>HelixSeek Business Cards</title>
<link href="https://fonts.googleapis.com/css2?family=Mulish:wght@300;400;600&family=Varela+Round&display=swap" rel="stylesheet">
<style>
  :root {
    --backdrop: #3a2418;
    --card-light: #ffffff;
    --card-mid: #e6e6e6;
    --card-dark: #cfcfcf;
    --mark-tone: rgba(150,150,150,0.28);
    --brand-blue: #1b86b8;
    --text-grey: #6a6a6a;
    --rule: #bdbdbd;
    --label: #1a1a1a;
  }
  * { box-sizing: border-box; margin: 0; padding: 0; }
  html, body { width: 1200px; height: 900px; overflow: hidden; }
  body {
    background: var(--backdrop);
    position: relative;
    font-family: "Mulish", sans-serif;
  }
  .card {
    position: absolute;
    overflow: hidden;
    background: linear-gradient(135deg, var(--card-light) 0%, var(--card-mid) 60%, var(--card-dark) 100%);
    box-shadow: 0 6px 16px rgba(0,0,0,0.45);
  }
  .card-back { width: 350px; height: 205px; top: 120px; }
  .card-back.variant-1 { left: 40px; }
  .card-back.variant-2 { left: 425px; }
  .card-back.variant-3 { left: 810px; }
  .variant-number {
    position: absolute; left: 18px; top: 16px;
    font-family: "Mulish", sans-serif; font-weight: 300;
    font-size: 38px; color: var(--label);
  }
  .backdrop-circle {
    position: absolute; border-radius: 50%;
    background: var(--mark-tone);
  }
  .variant-1 .backdrop-circle { width: 190px; height: 190px; left: 195px; top: -20px; }
  .variant-2 .backdrop-circle { width: 240px; height: 240px; left: 190px; top: -30px; }
  .variant-3 .backdrop-circle { width: 300px; height: 300px; left: 140px; top: -55px; }
  .brand {
    position: absolute; display: flex; align-items: center; gap: 6px;
    font-family: "Varela Round", sans-serif; color: var(--brand-blue);
  }
  .brand-dot { border-radius: 50%; background: var(--brand-blue); flex: none; }
  .card-back .brand { left: 22px; bottom: 22px; font-size: 21px; }
  .card-back .brand-dot { width: 18px; height: 18px; }

  .card-front { width: 400px; height: 244px; left: 400px; top: 560px; }
  .card-front .brand { left: 18px; top: 34px; font-size: 23px; }
  .card-front .brand-dot { width: 21px; height: 21px; }
  .card-front .backdrop-circle { width: 150px; height: 150px; left: 18px; top: 106px; }
  .holder { position: absolute; left: 180px; top: 88px; width: 200px; text-align: center; }
  .holder-name { font-size: 13px; color: var(--brand-blue); font-weight: 400; letter-spacing: 0.3px; }
  .holder-title { font-size: 9px; color: var(--brand-blue); margin-top: 4px; }
  .contacts {
    position: absolute; left: 184px; top: 156px;
    display: grid; grid-template-columns: 84px 120px; row-gap: 14px;
    font-size: 7.5px; color: var(--text-grey);
  }
  .contact-column { border-left: 1px solid var(--rule); padding: 6px 0 6px 8px; display: flex; flex-direction: column; gap: 14px; }
  .contact-line { display: flex; align-items: center; gap: 5px; white-space: nowrap; }
  .contact-line svg { width: 8px; height: 8px; flex: none; fill: var(--text-grey); }
  .contact-grid { position: absolute; left: 184px; top: 154px; display: flex; gap: 10px; font-size: 7.5px; color: var(--text-grey); }
  .address { position: absolute; right: 10px; bottom: 16px; font-size: 7px; color: var(--brand-blue); }
</style>
</head>
<body>
  <section class="card card-back variant-1">
    <span class="variant-number">1</span>
    <div class="backdrop-circle"></div>
    <div class="brand"><span class="brand-dot"></span>HelixSeek</div>
  </section>
  <section class="card card-back variant-2">
    <span class="variant-number">2</span>
    <div class="backdrop-circle"></div>
    <div class="brand"><span class="brand-dot"></span>HelixSeek</div>
  </section>
  <section class="card card-back variant-3">
    <span class="variant-number">3</span>
    <div class="backdrop-circle"></div>
    <div class="brand"><span class="brand-dot"></span>HelixSeek</div>
  </section>

  <section class="card card-front">
    <div class="brand"><span class="brand-dot"></span>HelixSeek</div>
    <div class="backdrop-circle"></div>
    <div class="holder">
      <p class="holder-name">Daniel Reyes</p>
      <p class="holder-title">General manager</p>
    </div>
    <div class="contact-grid">
      <div class="contact-column">
        <span class="contact-line"><svg viewBox="0 0 8 8"><rect x="2" y="0" width="4" height="8" rx="0.8"/></svg>00456789</span>
        <span class="contact-line"><svg viewBox="0 0 8 8"><circle cx="4" cy="4" r="3.6" fill="none" stroke="#6a6a6a" stroke-width="0.9"/><path d="M2.6 2.2 L3.5 2 L3.8 3.2 L3.3 3.6 Q3.9 4.6 4.7 5 L5.1 4.5 L6.2 4.8 L6 5.8 Q3.2 5.6 2.6 2.2Z"/></svg>111555667</span>
      </div>
      <div class="contact-column">
        <span class="contact-line"><span>@</span>reyes@helixseek.com</span>
        <span class="contact-line"><svg viewBox="0 0 8 8"><path d="M4 0.5 L8 4 L6.8 4 L6.8 7.5 L4.8 7.5 L4.8 5.3 L3.2 5.3 L3.2 7.5 L1.2 7.5 L1.2 4 L0 4Z"/></svg>www.helixseek.com</span>
      </div>
    </div>
    <p class="address">2400 North Ridge Road, Suite 120 Easton, MA 02356</p>
  </section>
</body>
</html>
```